New Podcast focussing on non-mainstream interventions for guidance needs podcast art

I need an exquisite piece of podcast art work for the launch of my new podcast 'Past the Hollow'. This podcast explores unorthodox, esoteric and unconventional methods to find peace, clarity and direction in life. Topics include family Constellations Systems, Psychedelics, Equine Therapy and Floatation to name a few. A teaser has been posted on Brevlo with a strong response. The audience is primarily midlifers or those in a career/personal crisis of direction. It's meant to comfort, inform and empower and offer other ways rather than mainstream to work out what to do with your life. The file shared with you shows the pic used on Brevlo as it's illustrating the idea of illumination. You can use it or not, and whilst I am ex-Military, I don't want the cover to convey an overly military influence. I'd like 'Past the Hollow' to feature on the art work and my name, Margot Pennick. I'd like inspiration, creativity, and the idea of hope conveyed as well as clarity and courage. Whilst the podcast is about finding your direction please do no use compass images or cross road images as that is too obvious.
Hope that all helps. Looking forward to your ideas.

```html
<!DOCTYPE html>
<html lang="en">
<head>
<meta charset="utf-8">
<title>Past the Hollow — Podcast Cover</title>
<link rel="stylesheet" href="https://fonts.googleapis.com/css2?family=Bebas+Neue&family=Montserrat:wght@600;700&display=swap">
<style>
  :root {
    --page-bg: #f2f2f2;
    --title-amber: #ffab00;
    --title-cream: #f3e3a0;
    --text-white: #ffffff;
    --scene-dark: #120607;
    --scene-mid: #4a1d1c;
    --scene-warm: #8a3c2a;
    --glow: #fff3ec;
  }
  * { margin: 0; padding: 0; box-sizing: border-box; }
  html, body {
    width: 1080px;
    height: 1200px;
    overflow: hidden;
    background: var(--page-bg);
  }
  .cover {
    position: absolute;
    left: 90px;
    top: 150px;
    width: 900px;
    height: 900px;
    overflow: hidden;
    background: var(--scene-dark);
  }
  .cover__scene {
    position: absolute;
    inset: 0;
    background:
      radial-gradient(circle at 68% 27%, var(--glow) 0, #f3b9b0 3%, rgba(180, 90, 110, 0.55) 12%, rgba(90, 30, 40, 0) 34%),
      radial-gradient(ellipse at 60% 90%, rgba(160, 70, 35, 0.75) 0, rgba(90, 35, 25, 0.4) 35%, rgba(0, 0, 0, 0) 65%),
      linear-gradient(180deg, #1e0a0c 0%, var(--scene-mid) 45%, var(--scene-warm) 78%, #2a0f0a 100%);
  }
  .cover__scene::after {
    content: "";
    position: absolute;
    inset: 0;
    background: linear-gradient(90deg, rgba(10, 3, 3, 0.85) 0%, rgba(10, 3, 3, 0.2) 45%, rgba(10, 3, 3, 0.35) 100%);
  }
  .title {
    position: absolute;
    left: 51px;
    top: 50px;
    font-family: "Bebas Neue", "Oswald", sans-serif;
    font-weight: 400;
    line-height: 1;
  }
  .title__line { display: block; }
  .title__line--past { color: var(--title-amber); font-size: 228px; height: 196px; }
  .title__line--the { color: var(--title-cream); font-size: 222px; height: 184px; }
  .title__line--hollow { color: var(--title-cream); font-size: 230px; }
  .credit {
    position: absolute;
    left: 54px;
    top: 755px;
    font-family: "Montserrat", "Helvetica Neue", sans-serif;
    color: var(--text-white);
  }
  .credit__label {
    display: block;
    font-size: 25px;
    font-weight: 600;
    letter-spacing: 0.5em;
    margin-bottom: 8px;
  }
  .credit__host {
    display: block;
    font-size: 40px;
    font-weight: 700;
    letter-spacing: -0.01em;
  }
  .credit__name { color: var(--title-amber); }
</style>
</head>
<body>
  <main class="cover">
    <div class="cover__scene" role="img" aria-label="Night photograph: a flare glowing in a dusky red sky above trees, a seated figure silhouetted in the foreground"></div>
    <h1 class="title">
      <span class="title__line title__line--past">PAST</span>
      <span class="title__line title__line--the">THE</span>
      <span class="title__line title__line--hollow">HOLLOW</span>
    </h1>
    <p class="credit">
      <span class="credit__label">PODCAST</span>
      <span class="credit__host">WITH <span class="credit__name">MARGOT PENNICK</span></span>
    </p>
  </main>
</body>
</html>
```